Orvel Crest Holdings Ltd
Creative Brief
Dara Kolby
COO
27B Hollin Row, London, E3 9TQ
dk@orvelcrest.co.uk
27b Hollin Row
Just the logo and the company's name on the green background

```html
<!DOCTYPE html>
<html lang="en">
<head>
<meta charset="utf-8">
<title>Orvel Crest Holdings Ltd — Business Card</title>
<link href="https://fonts.googleapis.com/css2?family=Cinzel:wght@500&family=Montserrat:wght@400;500;700&display=swap" rel="stylesheet">
<style>
  :root {
    --canvas: #d9d4c7;
    --card-white: #f7f6f2;
    --card-green: #3a3b2f;
    --gold: #b8945a;
    --ink: #2e2f27;
    --muted: #6d6c64;
    --rule: #cbb78f;
  }
  * { box-sizing: border-box; margin: 0; padding: 0; }
  html, body { width: 1200px; height: 901px; overflow: hidden; }
  body {
    background: var(--canvas);
    font-family: "Montserrat", sans-serif;
    display: flex;
    align-items: center;
    justify-content: center;
    gap: 60px;
  }
  .card {
    width: 520px;
    height: 300px;
    border-radius: 4px;
    position: relative;
    box-shadow: 0 10px 30px rgba(40, 38, 28, 0.18);
  }

  /* Front */
  .card-front {
    background: var(--card-white);
    display: flex;
    align-items: center;
  }
  .brand {
    width: 50%;
    display: flex;
    flex-direction: column;
    align-items: center;
    gap: 16px;
  }
  .brand-dot {
    width: 70px;
    height: 70px;
    border-radius: 50%;
    border: 2px solid var(--gold);
  }
  .brand-name {
    font-family: "Cinzel", serif;
    font-weight: 500;
    color: var(--gold);
    font-size: 17px;
    letter-spacing: 1.5px;
    text-align: center;
    line-height: 1.35;
    max-width: 190px;
  }
  .divider {
    width: 1px;
    height: 170px;
    background: var(--rule);
  }
  .contact {
    width: 50%;
    padding-left: 30px;
  }
  .person-name {
    font-weight: 700;
    font-size: 22px;
    letter-spacing: 1px;
    color: var(--ink);
  }
  .person-role {
    font-size: 11px;
    font-weight: 500;
    letter-spacing: 2px;
    color: var(--gold);
    margin-top: 4px;
    margin-bottom: 22px;
  }
  .contact-list { list-style: none; }
  .contact-list li {
    display: flex;
    align-items: center;
    gap: 9px;
    font-size: 11px;
    color: var(--muted);
    line-height: 1;
    margin-bottom: 9px;
  }
  .contact-list svg { width: 11px; height: 11px; flex: none; }

  /* Back */
  .card-back {
    background: var(--card-green);
    display: flex;
    flex-direction: column;
    align-items: center;
    justify-content: center;
    gap: 18px;
  }
  .card-back .brand-name { font-size: 20px; max-width: 240px; }
  .card-back .brand-dot { width: 84px; height: 84px; }
  .website {
    position: absolute;
    right: 18px;
    top: 50%;
    transform: translateY(-50%) rotate(90deg);
    transform-origin: center;
    font-size: 9px;
    letter-spacing: 3px;
    color: var(--gold);
    white-space: nowrap;
    width: 0;
    display: flex;
    justify-content: center;
  }
</style>
</head>
<body>
  <section class="card card-front">
    <div class="brand">
      <span class="brand-dot"></span>
      <p class="brand-name">Orvel Crest Holdings Ltd</p>
    </div>
    <span class="divider"></span>
    <div class="contact">
      <h1 class="person-name">DARA KOLBY</h1>
      <p class="person-role">COO</p>
      <ul class="contact-list">
        <li>
          <svg viewBox="0 0 12 12"><path d="M6 1a3.5 3.5 0 0 0-3.5 3.5C2.5 7.5 6 11 6 11s3.5-3.5 3.5-6.5A3.5 3.5 0 0 0 6 1zm0 4.8a1.3 1.3 0 1 1 0-2.6 1.3 1.3 0 0 1 0 2.6z" fill="#2e2f27"/></svg>
          <span>27b Hollin Row<br>London, E3 9TQ</span>
        </li>
        <li>
          <svg viewBox="0 0 12 12"><path d="M3 1.2l1.6 2.2-.9 1.2a6.5 6.5 0 0 0 3.7 3.7l1.2-.9 2.2 1.6-.8 1.8C6 10.8 1.2 6 1.2 2z" fill="#2e2f27"/></svg>
          <span>+44 (0)20 7946 0321</span>
        </li>
        <li>
          <svg viewBox="0 0 12 12"><rect x="3" y="0.8" width="6" height="10.4" rx="1" fill="none" stroke="#2e2f27" stroke-width="1.2"/><circle cx="6" cy="9.4" r="0.6" fill="#2e2f27"/></svg>
          <span>+44 (0)7700 900 482</span>
        </li>
        <li>
          <svg viewBox="0 0 12 12"><rect x="0.8" y="2.3" width="10.4" height="7.4" rx="0.8" fill="none" stroke="#2e2f27" stroke-width="1.1"/><path d="M1 2.8l5 3.8 5-3.8" fill="none" stroke="#2e2f27" stroke-width="1.1"/></svg>
          <span>dk@orvelcrest.co.uk</span>
        </li>
      </ul>
    </div>
  </section>

  <section class="card card-back">
    <span class="brand-dot"></span>
    <p class="brand-name">Orvel Crest Holdings Ltd</p>
    <p class="website"><span>www.orvelcrest.co.uk</span></p>
  </section>
</body>
</html>
```